OpenLeaf app needs an improved design

OpenLeaf makes available books that have been banned in certain countries. The current version of the app is available for download here: https://apps.vendrix-market.example/details?id=org.brightmoss.openleaf

At the moment, the app is available only in Chinese. Books are made available within the app, in text or audio format. Books can be downloaded for offline use. We created the app as a way to circumvent the intense censorship that is placed on book distribution inside China. The app is designed in such a way that the authorities are not able to censor the app, thus users in China are able to download the app, read content and receive updates to the app. So far over 100,000 people have used the app. Books are made available to the users for free and the app is also free to download.

We have used a similar anti-censorship strategy in a number of other apps, all with equally successful outcomes.

The app is only available on Android. While many Chinese purchase high end Android devices, Android is also the operating system of choice for new internet users in China. Oftentimes, the first time a user accesses the internet will be through an inexpensive Android smartphone.

This is very much a content driven app, with limited functionality but very visual. We need to optimize the app so that it is suitable for reading long texts. While we make available banned books through the app itself, our users are primarily avid readers - they are not likely to be netizens who wanted to download a book app just because it contains banned books. They will be readers who are interested in reading and exploring new books that are not normally available to them.

The app should have similar functionality to an e-reader, like a Pagette, however it needs to be optimized for smaller screens. Apps like Scrollnest present content in an easy to read format.

Target Market(s)

Our current end users are Chinese who are professionals and have an interest in reading. They are likely between the ages of 18-50. We try to make the app as easy and intuitive as possible. Even though there are over 700 million people online in China, another 600 million of them will come online soon. We want experienced internet and technology users to easily find the content they are looking for and we want new internet and technology users to be able to easily use the app. Our users mainly use the app in the comfort of their own home - as they would read an e-book (Pagette) or in a quiet cafe.

Industry/Entity Type

Book Publisher

Font styles to use
Serif

Colors

Designer to choose colors to be used in the design.

Requirements
Must have
• Our current challenges include:
• - We want to promote new books as well as popular books (and potentially other categories) and allow users to browse more books in that category.
• - Allow users to search.
• - For each book, we need an indication whether it is an audio book or a text book.
• - For each book, we need an indication whether the book has already been downloaded.
• Our current audio book challenges include:
• - Show book cover.
• - Include all standard audio playback functions (pause, play, next chapter etc).
• - Audio books can play in the background. When the user leaves this view, the app needs to indicate that an audio book is playing in the background, and show the user how to return to this interface (to pause playback, etc).
• Our current text book challenges include:
• - Show name of book.
• - Maximize use of screen (since it may be hard to read on a small device).
• - Allow user to easily navigate (next page, any page number etc).

```html
<!DOCTYPE html>
<html lang="en">
<head>
<meta charset="utf-8">
<title>OpenLeaf — Search</title>
<link rel="stylesheet" href="https://fonts.googleapis.com/css2?family=Source+Sans+3:wght@300;400;600&display=swap">
<style>
  :root {
    --accent: #1a8cef;
    --button: #1694ff;
    --text-light: #ffffff;
    --text-muted: #d9d9d9;
    --rule: #e6e6e6;
    --shade-top: #2a2724;
    --shade-mid: #1c1b1a;
    --shade-low: #141414;
  }
  html, body {
    margin: 0;
    padding: 0;
    width: 676px;
    height: 1200px;
    overflow: hidden;
    background: #000;
  }
  .screen {
    position: relative;
    width: 676px;
    height: 1200px;
    overflow: hidden;
    font-family: "Source Sans 3", "Myriad Pro", sans-serif;
    color: var(--text-light);
  }
  .backdrop {
    position: absolute;
    inset: 0;
    background:
      radial-gradient(ellipse at 70% 35%, rgba(70, 85, 95, 0.35), transparent 55%),
      radial-gradient(ellipse at 20% 80%, rgba(90, 70, 55, 0.35), transparent 60%),
      linear-gradient(180deg, var(--shade-top) 0%, var(--shade-mid) 45%, var(--shade-low) 100%);
  }
  .heading {
    position: absolute;
    top: 204px;
    left: 0;
    width: 676px;
    text-align: center;
  }
  .heading-title {
    margin: 0;
    padding-left: 14px;
    font-size: 35px;
    font-weight: 400;
    letter-spacing: 1px;
    color: var(--accent);
    line-height: 40px;
  }
  .heading-sub {
    margin: 4px 0 0;
    font-size: 24px;
    font-weight: 600;
    line-height: 28px;
  }
  .field {
    position: absolute;
    left: 105px;
    width: 464px;
    border-bottom: 1px solid var(--rule);
  }
  .field-label {
    display: block;
    font-size: 21px;
    font-weight: 400;
    color: var(--accent);
    line-height: 24px;
  }
  .field-value {
    display: block;
    font-size: 34px;
    font-weight: 300;
    line-height: 44px;
    padding-bottom: 4px;
  }
  .field-name { top: 335px; }
  .field-name .field-value { color: var(--text-muted); padding-left: 8px; }
  .field-category { top: 540px; }
  .field-category .field-value { padding-left: 14px; }
  .field-arrow {
    position: absolute;
    right: 10px;
    bottom: 18px;
  }
  .divider-word {
    position: absolute;
    left: 0;
    width: 660px;
    text-align: center;
    font-size: 33px;
    font-weight: 300;
    line-height: 36px;
  }
  .divider-first { top: 473px; }
  .divider-second { top: 857px; }
  .action {
    position: absolute;
    left: 106px;
    width: 464px;
    height: 79px;
    border-radius: 3px;
    background: var(--button);
    color: var(--text-light);
    font-size: 35px;
    font-weight: 400;
    letter-spacing: 1.5px;
    line-height: 79px;
    text-align: center;
  }
  .action-search { top: 746px; }
  .action-browse { top: 921px; }
  .help {
    position: absolute;
    top: 1118px;
    left: 0;
    width: 676px;
    text-align: center;
    font-size: 24px;
    font-weight: 400;
    line-height: 30px;
  }
  .help-link {
    color: var(--accent);
    text-decoration: underline;
  }
</style>
</head>
<body>
  <main class="screen">
    <div class="backdrop" role="img" aria-label="Dimmed photograph of a bookshelf filled with books"></div>

    <header class="heading">
      <h1 class="heading-title">SEARCH</h1>
      <p class="heading-sub">from sms</p>
    </header>

    <div class="field field-name">
      <span class="field-label">By Name</span>
      <span class="field-value">Enter book or author name</span>
    </div>

    <div class="divider-word divider-first">OR</div>

    <div class="field field-category">
      <span class="field-label">By Category</span>
      <span class="field-value">Select</span>
      <svg class="field-arrow" width="22" height="14" viewBox="0 0 22 14" aria-hidden="true">
        <polygon points="0,0 22,0 11,14" fill="#ffffff"/>
      </svg>
    </div>

    <div class="action action-search">SEARCH</div>

    <div class="divider-word divider-second">OR</div>

    <div class="action action-browse">BROWSE BOOKS</div>

    <p class="help">Need Help ? <span class="help-link">Contact Us</span></p>
  </main>
</body>
</html>
```